Business Card Design Project

We are a commercial talent casting company, a very "now" company. We need a new business card that is both current, graphic and elegantly interesting. As we are a service business,
we need something that will attract the attention of new clients,
yet project a business that is 25 years old.

Industry/Entity Type

Business

Requirements
Must have
• 1. Logo - Nora Quillan Casting
2. Address - 47 Harwick Street
New York, New York 10027
3. Phone - 212-638-4170
4. E-Mail - Casting@noraquillan.com

Nice to have
• Would like the card in black and white with the only accent
color being red.

```html
<!DOCTYPE html>
<html lang="en">
<head>
<meta charset="utf-8">
<title>Nora Quillan Casting — Business Card</title>
<link rel="stylesheet" href="https://fonts.googleapis.com/css2?family=Michroma&display=swap">
<style>
  :root {
    --ink: #000000;
    --paper: #ffffff;
    --stage: #e6e6e6;
    --card-w: 660px;
    --card-h: 400px;
    --band-w: 178px;
  }
  * { box-sizing: border-box; margin: 0; padding: 0; }
  html, body {
    width: 1200px;
    height: 900px;
    overflow: hidden;
  }
  body {
    background: var(--stage);
    font-family: "Michroma", "Helvetica Neue", Arial, sans-serif;
    display: flex;
    flex-direction: column;
    align-items: center;
    justify-content: center;
    gap: 40px;
  }
  .card {
    position: relative;
    width: var(--card-w);
    height: var(--card-h);
    overflow: hidden;
  }
  .card--front { background: var(--ink); color: var(--paper); }
  .card--back  { background: var(--paper); color: var(--ink); }

  .card__band {
    position: absolute;
    top: 0;
    left: 0;
    width: var(--band-w);
    height: 100%;
  }
  .card--front .card__band { background: var(--paper); }
  .card--back  .card__band { background: var(--ink); }

  .brand {
    position: absolute;
    top: 62px;
    left: calc(var(--band-w) + 40px);
    display: flex;
    align-items: flex-start;
    gap: 22px;
  }
  .brand__dot {
    width: 34px;
    height: 34px;
    margin-top: 4px;
    border-radius: 50%;
    border: 3px solid currentColor;
  }
  .brand__name {
    font-size: 21px;
    line-height: 1.45;
    letter-spacing: 0.14em;
    text-transform: uppercase;
    font-weight: 400;
  }
  .brand__name span { display: block; }

  .contact {
    position: absolute;
    right: 28px;
    bottom: 26px;
    text-align: right;
    font-style: normal;
    font-size: 15px;
    line-height: 1.5;
    letter-spacing: 0.1em;
    font-variant: small-caps;
  }
  .contact__address { margin-bottom: 22px; }
  .contact p { white-space: nowrap; }
</style>
</head>
<body>
  <section class="card card--front" aria-label="Business card front">
    <div class="card__band"></div>
    <div class="brand">
      <span class="brand__dot" aria-hidden="true"></span>
      <h1 class="brand__name"><span>Nora</span><span>Quillan</span><span>Casting</span></h1>
    </div>
    <address class="contact">
      <div class="contact__address">
        <p>47 Harwick Street</p>
        <p>New York, New York 10027</p>
      </div>
      <p>212-638-4170</p>
      <p>Casting@noraquillan.com</p>
    </address>
  </section>

  <section class="card card--back" aria-label="Business card back">
    <div class="card__band"></div>
    <div class="brand">
      <span class="brand__dot" aria-hidden="true"></span>
      <h2 class="brand__name"><span>Nora</span><span>Quillan</span><span>Casting</span></h2>
    </div>
    <address class="contact">
      <div class="contact__address">
        <p>47 Harwick Street</p>
        <p>New York, New York 10027</p>
      </div>
      <p>212-638-4170</p>
      <p>Casting@noraquillan.com</p>
    </address>
  </section>
</body>
</html>
```